New Packaging Design Project

Wine packaging redesign. Retail partner requested a redesign of a private label wine. The old label is attached. Our partner liked the Lantern and Briar label and wanted something similar. There will be a logo added to the top of the label

Went on vacation/holiday

```html
<!DOCTYPE html>
<html lang="en">
<head>
<meta charset="utf-8">
<title>Lantern &amp; Briar – Sonoma Coast Chardonnay 2018 Label</title>
<link rel="stylesheet" href="https://fonts.googleapis.com/css2?family=Libre+Bodoni:wght@700&display=swap">
<style>
  :root {
    --backdrop: #cbc7c7;
    --ink: #141414;
    --veil: rgba(255, 255, 255, 0.22);
    --art-top: #dcdfdc;
    --art-mid: #9fab8e;
    --art-bottom: #4f7773;
  }
  * { margin: 0; padding: 0; box-sizing: border-box; }
  html, body {
    width: 1200px;
    height: 3154px;
    overflow: hidden;
    background: var(--backdrop);
  }
  .canvas {
    position: relative;
    width: 1200px;
    height: 3154px;
    background: var(--backdrop);
  }
  .label {
    position: absolute;
    left: 100px;
    top: 792px;
    width: 1000px;
    height: 1570px;
    overflow: hidden;
  }
  .label-artwork {
    position: absolute;
    inset: 0;
    background: linear-gradient(180deg, var(--art-top) 0%, var(--art-mid) 50%, var(--art-bottom) 100%);
  }
  .title-veil {
    position: absolute;
    left: 32px;
    top: 207px;
    width: 936px;
    height: 858px;
    background: var(--veil);
  }
  .label-text {
    position: absolute;
    left: 0;
    width: 100%;
    text-align: center;
    font-family: "Libre Bodoni", "Bodoni Moda", serif;
    font-weight: 700;
    color: var(--ink);
    line-height: 1;
    white-space: nowrap;
  }
  .brand-name  { top: 350px; font-size: 80px; letter-spacing: 1px; }
  .region      { top: 489px; font-size: 46px; letter-spacing: 1px; }
  .conjunction { top: 566px; font-size: 18px; letter-spacing: 2px; }
  .varietal    { top: 639px; font-size: 50px; letter-spacing: 1px; }
  .vintage     { top: 738px; font-size: 40px; letter-spacing: 2px; }
</style>
</head>
<body>
  <main class="canvas">
    <section class="label">
      <div class="label-artwork" role="img" aria-label="Watercolour illustration of a birch forest under a pale sky"></div>
      <div class="title-veil"></div>
      <h1 class="label-text brand-name">LANTERN &amp; BRIAR</h1>
      <p class="label-text region">SONOMA COAST</p>
      <p class="label-text conjunction">AND</p>
      <p class="label-text varietal">CHARDONNAY</p>
      <p class="label-text vintage">2018</p>
    </section>
  </main>
</body>
</html>
```